Design for iOS app - Scanner App

We are developing an iOS app that is scanning receipts and mailing them to a predefined email address. The app should work more or less like TallySnap app (a short demo of the TallySnap app is available here: https://www.clipvault.example/watch?v=QmRtZpLwXkA).

We have prototyped the app in the link below:
http://app.wirepane.example/view/a71c3d9f2b8e40c6d5f18e27b9a4c3d0

NB!: Please do not follow the mockups literally, but the iOS Human Interface Guidelines!

The technical specifications and descriptions of the app's functionalities are available in the link below:
https://sheets.papyrdesk.example/document/d/9pQrx-TW2cNmbvJLhQ7dKzR4eWs-aY_3Hkv8Tfmn5xe/edit?usp=sharing

Requirements for the design:

- The design should be provided as PSD, where each page/section should be in its own PSD file OR all pages/sections should be represented as folder groups in a single PSD file.

- All graphical elements in the design should be delivered as single layers which can then be extracted from the PSD.

- All graphical elements (icons, graphical buttons, etc.) should be provided as vector objects in the PSD, so that they can be exported into different sizes without loss of quality (for responsiveness).

- The design should use either web safe fonts or Quorby Fonts.

Instructions for the design:

The design should have habitual user interface like ordinary iOS navigation stack, with navigation bar on the top and all other elements on the bottom. That means just to make the top bar in your app be more like iOS. Please follow the iOS Human Interface Guidelines, not the mockups literally .
FX: the e small elements in Dimensions screen like delete icons and active checkbox. In
https://devhub.orchardly.example/library/ios/documentation/UserExperience/Conceptual/MobileHIG/LayoutandAppearance.html#//ref/doc/uid/TP51208847-CH31-SW1
is described that interface elements should be at least 44x44 px - it's normal practice for all mobile development (iOS, android), so you should consider this too.

Please also provide an app icon and suggest a logo for the app.

Requirements
Must have
• Please make sure that the design is flat. Like iOS app, Pagefold, Quorby apps etc.
Nice to have
• The design could be somewhat like the design for Mindvale Pagefold(https://apps.orchardly.example/bg/app/mindvale-pagefold/id552719043?mt=8) without being too similar
Should not have
• 3D look

```html
<!DOCTYPE html>
<html lang="en">
<head>
<meta charset="utf-8">
<title>TallySnap – Scan</title>
<link rel="stylesheet" href="https://fonts.googleapis.com/css2?family=Roboto:wght@300;400;500&display=swap">
<style>
  :root {
    --blue-top: #33457a;
    --blue-bottom: #4163a0;
    --band: rgba(120, 150, 200, 0.16);
    --ring: rgba(255, 255, 255, 0.55);
    --ring-faint: rgba(255, 255, 255, 0.10);
    --white: #ffffff;
    --pending: #f76f72;
    --pending-edge: #c4565a;
    --sent: #62b1fd;
    --sent-edge: #3f80c2;
    --badge: #2f4a78;
    --muted: #d9dde3;
    --track: #f1f1f1;
    --fill: #97a3b6;
  }
  html, body {
    margin: 0;
    padding: 0;
    width: 708px;
    height: 1200px;
    overflow: hidden;
    background: var(--white);
    font-family: "Roboto", sans-serif;
  }
  .screen {
    position: relative;
    width: 708px;
    height: 1200px;
    overflow: hidden;
  }
  .hero {
    position: absolute;
    inset: 0 0 auto 0;
    height: 737px;
    background: linear-gradient(180deg, var(--blue-top), var(--blue-bottom));
  }
  .hero-band {
    position: absolute;
    inset: 0;
  }
  .status-bar {
    position: absolute;
    top: 8px;
    left: 22px;
    right: 22px;
    height: 28px;
    color: var(--white);
    font-size: 20px;
    font-weight: 500;
    display: flex;
    align-items: center;
    justify-content: space-between;
  }
  .status-left, .status-right { display: flex; align-items: center; gap: 8px; }
  .status-time { position: absolute; left: 50%; transform: translateX(-50%); }
  .nav-title {
    position: absolute;
    top: 62px;
    left: 0;
    right: 0;
    text-align: center;
    color: var(--white);
    font-size: 30px;
    font-weight: 400;
  }
  .nav-settings {
    position: absolute;
    top: 58px;
    left: 620px;
    width: 42px;
    height: 42px;
  }
  .scan-dial {
    position: absolute;
    left: 104px;
    top: 174px;
    width: 500px;
    height: 500px;
  }
  .scan-label {
    position: absolute;
    left: 0;
    right: 0;
    top: 391px;
    text-align: center;
    color: rgba(255, 255, 255, 0.82);
    font-size: 70px;
    font-weight: 300;
    letter-spacing: 1px;
  }
  .queue-button {
    position: absolute;
    top: 832px;
    width: 240px;
    height: 63px;
    border: none;
    border-radius: 4px;
    color: var(--white);
    font-family: "Roboto", sans-serif;
    font-size: 27px;
    font-weight: 300;
  }
  .queue-button--pending { left: 87px; background: var(--pending); box-shadow: 0 3px 0 var(--pending-edge); }
  .queue-button--sent { left: 394px; background: var(--sent); box-shadow: 0 3px 0 var(--sent-edge); }
  .queue-badge {
    position: absolute;
    top: -10px;
    right: -8px;
    width: 38px;
    height: 38px;
    border-radius: 50%;
    background: var(--badge);
    color: var(--white);
    font-size: 20px;
    line-height: 38px;
    text-align: center;
  }
  .upload-label {
    position: absolute;
    top: 1054px;
    left: 0;
    right: 0;
    text-align: center;
    color: var(--muted);
    font-size: 21px;
    font-weight: 300;
  }
  .upload-track {
    position: absolute;
    top: 1108px;
    left: 68px;
    width: 585px;
    height: 26px;
    background: var(--track);
  }
  .upload-fill { width: 230px; height: 100%; background: var(--fill); }
</style>
</head>
<body>
<main class="screen">
  <section class="hero">
    <svg class="hero-band" width="708" height="737" viewBox="0 0 708 737" aria-hidden="true">
      <polygon points="368,0 708,0 708,737 695,737" fill="var(--band)"/>
    </svg>

    <header class="status-bar">
      <div class="status-left">
        <svg width="64" height="14" viewBox="0 0 64 14" aria-hidden="true">
          <circle cx="6" cy="7" r="5.5" fill="#fff"/>
          <circle cx="19" cy="7" r="5.5" fill="#fff"/>
          <circle cx="32" cy="7" r="5.5" fill="#fff"/>
          <circle cx="45" cy="7" r="5" fill="none" stroke="#fff" stroke-width="1.2"/>
          <circle cx="58" cy="7" r="5" fill="none" stroke="#fff" stroke-width="1.2"/>
        </svg>
        <span class="status-carrier">KESTREL</span>
        <svg width="22" height="16" viewBox="0 0 22 16" aria-hidden="true">
          <path d="M1 5a15 15 0 0 1 20 0" fill="none" stroke="#fff" stroke-width="2.2"/>
          <path d="M5 9a9 9 0 0 1 12 0" fill="none" stroke="#fff" stroke-width="2.2"/>
          <circle cx="11" cy="13.5" r="2.2" fill="#fff"/>
        </svg>
      </div>
      <span class="status-time">4:21 PM</span>
      <div class="status-right">
        <svg width="12" height="20" viewBox="0 0 12 20" aria-hidden="true">
          <path d="M1 5l10 9-5 5V1l5 5-10 9" fill="none" stroke="rgba(255,255,255,0.7)" stroke-width="1.5"/>
        </svg>
        <span>100%</span>
        <svg width="46" height="20" viewBox="0 0 46 20" aria-hidden="true">
          <rect x="1" y="2" width="40" height="16" rx="3" fill="none" stroke="#fff" stroke-width="1.5"/>
          <rect x="3.5" y="4.5" width="35" height="11" rx="1.5" fill="#fff"/>
          <rect x="42.5" y="7" width="2.5" height="6" rx="1" fill="#fff"/>
        </svg>
      </div>
    </header>

    <h1 class="nav-title">TallySnap</h1>
    <svg class="nav-settings" viewBox="0 0 42 42" aria-label="Settings" role="img">
      <g fill="none" stroke="#fff" stroke-width="2">
        <path d="M18 4h6l1 5 4 2 4-3 4 4-3 4 2 4 5 1v6l-5 1-2 4 3 4-4 4-4-3-4 2-1 5h-6l-1-5-4-2-4 3-4-4 3-4-2-4-5-1v-6l5-1 2-4-3-4 4-4 4 3 4-2z" stroke-linejoin="round"/>
        <circle cx="21" cy="21" r="6"/>
      </g>
    </svg>

    <svg class="scan-dial" viewBox="0 0 500 500" aria-hidden="true">
      <circle cx="250" cy="250" r="245" fill="none" stroke="var(--ring-faint)" stroke-width="1.5"/>
      <circle cx="250" cy="250" r="175" fill="none" stroke="var(--ring)" stroke-width="1.8"/>
      <path d="M250 75 A175 175 0 0 1 425 250" fill="none" stroke="#fff" stroke-width="5"/>
    </svg>
    <div class="scan-label">SCAN</div>
  </section>

  <button class="queue-button queue-button--pending">Pending<span class="queue-badge">3</span></button>
  <button class="queue-button queue-button--sent">Sent</button>

  <p class="upload-label">Sending an Email :</p>
  <div class="upload-track"><div class="upload-fill"></div></div>
</main>
</body>
</html>
```